Kelekeleoliolimaiwaipeleke Fish Package

We need a package design for our Kelekeleoliolimaiwaipeleke Fish (not Bravlin fish). We plan to sell them at Hawaii stores to start and them take them to the mainland. We are looking for a package design that includes the front with a Kelekeleoliolimaiwaipeleke Fish (not a photo) and a back design with a photo of the fish (we will supply), information about the fish and nutrition information.

Target Market(s)

Premium market

Colors

Designer to choose colors to be used in the design.

Requirements
Must have
• See attached overview - also, it must include our logo (which we will provide)
Nice to have
• See attached overview

```html
<!DOCTYPE html>
<html lang="en">
<head>
<meta charset="UTF-8">
<title>Kelekeleoliolimaiwaipeleke Fish Package</title>
<link rel="stylesheet" href="https://fonts.googleapis.com/css2?family=Bebas+Neue&display=swap">
<style>
  :root {
    --stage: #e9e9e9;
    --red-deep: #5e0006;
    --red-mid: #9a0009;
    --red-bright: #c8000c;
    --swoosh: #e8293b;
    --band-grey: #666666;
    --sea-deep: #1b3f8e;
    --sea-mid: #2a5fb0;
    --sea-light: #4f86b8;
    --fish-light: #e6e1cf;
    --fish-mid: #b9b08a;
    --fish-dark: #6d6a55;
    --white: #ffffff;
    --brand-red: #e8303c;
  }
  * { margin: 0; padding: 0; box-sizing: border-box; }
  html, body {
    width: 994px;
    height: 1200px;
    overflow: hidden;
    background: var(--stage);
  }
  .package-front {
    position: absolute;
    left: 34px;
    top: 0;
    width: 926px;
    height: 1200px;
    overflow: hidden;
    font-family: "Bebas Neue", "Oswald", sans-serif;
    color: var(--white);
  }
  .package-art {
    position: absolute;
    inset: 0;
    width: 926px;
    height: 1200px;
  }
  .brand-tab {
    position: absolute;
    left: 129px;
    top: 0;
    width: 667px;
    height: 258px;
    background: var(--white);
    border-radius: 0 0 34px 34px;
    display: flex;
    align-items: center;
    justify-content: center;
    padding-top: 30px;
  }
  .brand-name {
    font-size: 124px;
    line-height: 1;
    letter-spacing: 10px;
    color: var(--brand-red);
    font-weight: 400;
  }
  .product-title {
    position: absolute;
    left: 68px;
    top: 328px;
    font-size: 70px;
    line-height: 1;
    white-space: nowrap;
    font-weight: 400;
  }
  .tagline-band {
    position: absolute;
    left: 0;
    top: 435px;
    width: 860px;
    height: 131px;
    background: var(--band-grey);
    padding: 18px 0 0 68px;
  }
  .tagline {
    font-size: 48px;
    line-height: 52px;
    font-weight: 400;
    white-space: nowrap;
  }
  .product-details {
    position: absolute;
    left: 0;
    width: 926px;
    top: 1020px;
    text-align: center;
    font-size: 36px;
    line-height: 40px;
    font-weight: 400;
  }
</style>
</head>
<body>
  <main class="package-front">
    <svg class="package-art" viewBox="0 0 926 1200" xmlns="http://www.w3.org/2000/svg">
      <defs>
        <linearGradient id="redField" x1="0" y1="0" x2="0.3" y2="1">
          <stop offset="0" stop-color="var(--red-deep)"/>
          <stop offset="0.45" stop-color="var(--red-mid)"/>
          <stop offset="1" stop-color="var(--red-bright)"/>
        </linearGradient>
        <linearGradient id="seaField" x1="0" y1="0" x2="1" y2="1">
          <stop offset="0" stop-color="var(--sea-light)"/>
          <stop offset="0.5" stop-color="var(--sea-mid)"/>
          <stop offset="1" stop-color="var(--sea-deep)"/>
        </linearGradient>
        <linearGradient id="fishTone" x1="0" y1="0" x2="1" y2="0">
          <stop offset="0" stop-color="var(--fish-light)"/>
          <stop offset="0.5" stop-color="var(--fish-mid)"/>
          <stop offset="1" stop-color="var(--fish-light)"/>
        </linearGradient>
      </defs>
      <rect class="red-field" width="926" height="1200" fill="url(#redField)"/>
      <path class="swoosh" fill="var(--swoosh)"
        d="M926,299 C800,560 470,650 280,760 C150,835 50,900 0,960 L0,1200 L926,1200 Z"/>
      <path class="reef-photo" role="img" aria-label="Underwater reef photo in deep blue water"
        fill="url(#seaField)"
        d="M926,415 C810,600 520,700 330,790 C180,860 60,940 0,1005 L0,1200 L926,1200 Z"/>
      <rect class="fish-photo" role="img" aria-label="Photo of a striped reef triggerfish swimming to the right"
        x="195" y="703" width="578" height="264" rx="40" fill="url(#fishTone)" opacity="0.85"/>
    </svg>

    <header class="brand-tab">
      <span class="brand-name">KOA BITES</span>
    </header>

    <h1 class="product-title">KELEKELEOLIOLIMAIWAIPELEKE FISH</h1>

    <div class="tagline-band">
      <p class="tagline">PREMIUM KELEKELEOLIOLIMAIWAIPELEKE<br>FISH A HAWAIIAN TREAT</p>
    </div>

    <p class="product-details">PINEAPPLE, CITRUS AND RASPBERRY<br>NET WEIGHT 5.0 OZ</p>
  </main>
</body>
</html>
```